Corvane Link Marketing Website

Corvane Link is the brand for a series of nation-wide internet peering exchanges operated by the Tallowmere Network Society Inc. (TNSI), a not-for-profit association founded in 1995.

Our current website is built on Drupal, and we are looking to migrate to WordPress with a similarly clean and modern theme:

http://www.corvanelink.example/

Target Market(s)

Technical and professional staff from the telecommunications industry in Australia.

Industry/Entity Type

Telecom

Font styles to use
Sans Serif

Requirements
Must have
• Responsive layout for mobile viewers
• Compatible with WordPress 4.2.2 and PHP 5.5.
• Winning entry will provide a completed WordPress theme file compatible .
• Usage of the "Corvane Link" logo must comply with the attached style guide.

```html
<!DOCTYPE html>
<html lang="en">
<head>
<meta charset="utf-8">
<title>Corvane Link – Not-for-profit Internet Peering Exchanges</title>
<link href="https://fonts.googleapis.com/css2?family=Open+Sans:ital,wght@0,400;0,600;0,700;1,400&family=Roboto+Condensed:wght@700&display=swap" rel="stylesheet">
<style>
:root{
  --blue:#1f7dc6;
  --blue-dark:#176aab;
  --navy:#0e2a4a;
  --orange:#f39a1e;
  --text:#555b62;
  --heading:#2a3440;
  --light:#f1f2f4;
  --footer:#ececec;
  --bottom:#2c2f33;
  --white:#ffffff;
}
*{box-sizing:border-box;margin:0;padding:0}
html,body{width:1200px;height:2288px;overflow:hidden}
body{font-family:"Open Sans",Arial,sans-serif;color:var(--text);background:var(--white);font-size:13px;line-height:1.55}
.wrap{width:1040px;margin:0 auto;position:relative}

/* header */
.site-header{height:100px;background:var(--white);border-bottom:1px solid #e3e5e8}
.site-header .wrap{height:100%;display:flex;align-items:center;justify-content:space-between}
.brand{display:flex;align-items:center;gap:10px}
.brand-mark{width:30px;height:30px;background:var(--blue)}
.brand-name{font-weight:700;font-size:24px;color:var(--blue);letter-spacing:.5px}
.brand-tag{font-size:10px;color:#8a9099;margin-top:-2px}
.header-right{text-align:right}
.contact-line{font-size:11px;color:#7a8088;display:flex;gap:22px;justify-content:flex-end;align-items:center}
.contact-line span{display:flex;align-items:center;gap:6px}
.main-nav{display:flex;gap:34px;margin-top:14px;justify-content:flex-end}
.main-nav a{font-size:11px;font-weight:700;color:#6a717a;text-decoration:none;text-transform:uppercase;letter-spacing:.5px;padding-bottom:6px}
.main-nav a.active{color:var(--blue);border-bottom:3px solid var(--blue)}
.dropdown{position:absolute;left:680px;top:101px;width:220px;background:var(--orange);z-index:5}
.dropdown a{display:block;color:var(--white);font-size:11px;padding:6px 14px;text-decoration:none}
.dropdown a+a{background:var(--blue)}

/* hero */
.hero{height:460px;position:relative;background:linear-gradient(100deg,#0b2746 0%,#1d4f80 45%,#8fb4d2 80%,#cfdde9 100%)}
.hero-image{position:absolute;inset:0}
.hero .wrap{padding-top:218px}
.hero-kicker{font-family:"Roboto Condensed",Arial,sans-serif;font-size:42px;color:var(--white);letter-spacing:1px;line-height:1}
.hero-title{font-family:"Roboto Condensed",Arial,sans-serif;font-size:27px;color:var(--white);line-height:1.2;margin-top:10px;width:620px}
.btn{display:inline-block;background:var(--blue);color:var(--white);font-size:11px;font-weight:700;text-transform:uppercase;padding:11px 26px;border-radius:3px;text-decoration:none}
.hero .btn{margin-top:28px}

/* intro */
.intro{height:120px;background:var(--light);border-bottom:1px solid #e1e3e6}
.intro .wrap{height:100%;display:flex;align-items:center;justify-content:space-between}
.intro p{font-style:italic;font-size:15px;color:#68707a;width:760px;line-height:1.5}
.intro .btn{padding:12px 34px}

/* features */
.features{height:248px}
.features .wrap{display:flex;justify-content:space-between;padding-top:34px}
.feature{width:300px;text-align:center}
.feature-icon{width:66px;height:66px;border-radius:50%;border:2px solid var(--blue);margin:0 auto;display:flex;align-items:center;justify-content:center}
.feature h3{font-size:15px;font-weight:700;color:var(--blue);margin-top:16px;text-transform:uppercase;letter-spacing:.5px}
.feature p{font-size:11px;margin-top:10px;line-height:1.6}
.feature .more{color:var(--blue);font-size:11px}

/* benefits */
.benefits{height:400px;background:var(--blue)}
.benefits .wrap{display:flex;height:100%}
.person-photo{width:300px;height:360px;margin-top:40px;background:linear-gradient(180deg,#2b8ad2 0%,#1a5f99 60%,#16324f 100%)}
.benefit-list{flex:1;padding:26px 0 0 50px;list-style:none}
.benefit{display:flex;gap:14px;margin-bottom:14px}
.benefit-icon{flex:none;width:22px;height:22px;border-radius:50%;background:var(--white);display:flex;align-items:center;justify-content:center}
.benefit h4{font-size:11px;font-weight:700;color:var(--white);text-transform:uppercase}
.benefit p{font-size:10.5px;color:#d9e9f6;line-height:1.5;margin-top:2px}

/* posts + testimonials */
.news{height:360px}
.news .wrap{display:flex;justify-content:space-between;padding-top:40px}
.section-title{font-size:19px;font-weight:700;color:var(--heading);text-transform:uppercase;padding-bottom:10px;border-bottom:1px solid #dfe2e6;position:relative}
.section-title::after{content:"";position:absolute;left:0;bottom:-2px;width:60px;height:3px;background:var(--blue)}
.blog{width:470px}
.post{display:flex;gap:16px;margin-top:22px}
.post-thumb{flex:none;width:70px;height:70px;background:linear-gradient(135deg,#5b6f84,#a8b7c6)}
.post h5{font-size:12px;font-weight:700;color:var(--heading)}
.post p{font-size:11px;margin-top:4px}
.read-more{display:block;text-align:right;font-size:11px;color:var(--heading);margin-top:14px}
.testimonials{width:520px}
.quote{display:flex;gap:18px;margin-top:24px}
.quote-mark{font-size:64px;line-height:.8;color:var(--blue);font-weight:700}
.quote p{font-size:11px;line-height:1.6}
.quote-author{display:flex;align-items:center;gap:12px;justify-content:flex-end;margin-top:12px}
.avatar{width:44px;height:44px;border-radius:50%;background:linear-gradient(135deg,#b9c3cd,#7a8896)}
.quote-author strong{display:block;font-size:11px;color:var(--heading)}
.quote-author small{font-size:10px;color:#8a9099}

/* partners */
.partners{height:220px;border-top:1px solid #e3e5e8;border-bottom:1px solid #e3e5e8}
.partners .wrap{height:100%;display:flex;align-items:center;justify-content:space-between}
.partner{font-size:30px;font-weight:700;color:#3a3f45}

/* footer */
.site-footer{height:320px;background:var(--footer)}
.site-footer .wrap{display:flex;justify-content:space-between;padding-top:34px}
.site-footer h3{font-size:22px;font-weight:400;color:var(--heading)}
.site-footer .lead{font-size:11px;margin-top:6px}
.touch{width:480px}
.touch-body{display:flex;gap:20px;margin-top:22px}
.touch-list{list-style:none;font-size:11px;width:190px}
.touch-list li{display:flex;gap:10px;margin-bottom:14px;align-items:flex-start}
.map{width:260px;height:170px;background:linear-gradient(135deg,#e6e9dc,#cfd8c4)}
.social{width:500px}
.social-grid{display:grid;grid-template-columns:repeat(3,1fr);gap:14px;margin-top:26px}
.social-btn{background:var(--white);border:1px solid #d6d9dd;height:40px;display:flex;align-items:center;justify-content:center;gap:8px;font-size:11px;color:#5f666e}
.social-btn i{width:10px;height:10px;background:var(--blue);display:block}
.bottom-bar{height:48px;background:var(--bottom);color:#a7adb3;font-size:11px;display:flex;align-items:center;justify-content:center}
</style>
</head>
<body>

<header class="site-header">
  <div class="wrap">
    <div class="brand">
      <span class="brand-mark"></span>
      <div>
        <div class="brand-name">Corvane Link</div>
        <div class="brand-tag">Tallowmere Network Society Inc.</div>
      </div>
    </div>
    <div class="header-right">
      <div class="contact-line">
        <span><svg width="10" height="10" viewBox="0 0 10 10"><path d="M2 0l2 2-1 2c1 1 2 2 3 3l2-1 2 2-2 2C4 10 0 6 0 2z" fill="#1f7dc6"/></svg>+61 8 5550 0142</span>
        <span><svg width="12" height="9" viewBox="0 0 12 9"><rect x=".5" y=".5" width="11" height="8" fill="none" stroke="#1f7dc6"/><path d="M.5.5l5.5 4 5.5-4" fill="none" stroke="#1f7dc6"/></svg>hello@corvanelink.example</span>
      </div>
      <nav class="main-nav">
        <a href="#" class="active">Home</a>
        <a href="#">Services ▾</a>
        <a href="#">Organisation ▾</a>
        <a href="#">Blog</a>
        <a href="#">Contact</a>
      </nav>
    </div>
  </div>
</header>

<div class="dropdown">
  <a href="#">Peering ▸</a>
  <a href="#">Members Portal</a>
</div>

<section class="hero">
  <div class="hero-image" role="img" aria-label="Close-up photo of hands typing on a laptop keyboard in blue light"></div>
  <div class="wrap">
    <div class="hero-kicker">NOT-FOR-PROFIT</div>
    <h1 class="hero-title">AUSTRALIA'S ONLY NOT-FOR-PROFIT AND INDEPENDENT INTERNET PEERING EXCHANGES</h1>
    <a href="#" class="btn">Get Started</a>
  </div>
</section>

<section class="intro">
  <div class="wrap">
    <p>We are the country's only not-for-profit and independent internet peering provider. Member owned, carrier neutral, with proven high quality peering services since 1995!</p>
    <a href="#" class="btn">Read More</a>
  </div>
</section>

<section class="features">
  <div class="wrap">
    <div class="feature">
      <div class="feature-icon"><svg width="30" height="30" viewBox="0 0 30 30" fill="#1f7dc6"><circle cx="10" cy="10" r="5"/><circle cx="21" cy="11" r="4"/><path d="M1 26c0-7 4-10 9-10s9 3 9 10zM17 17c6-1 11 2 11 9h-7c0-4-1-7-4-9z"/></svg></div>
      <h3>Member Owned</h3>
      <p>Corvane Link is owned and operated by the Tallowmere Network Society Inc. (TNSI), a not-for-profit body run by its members. To get involved please contact <span class="more">members@corvanelink.example</span></p>
    </div>
    <div class="feature">
      <div class="feature-icon"><svg width="30" height="30" viewBox="0 0 30 30" fill="none" stroke="#1f7dc6" stroke-width="2"><path d="M15 4v22M6 26h18M4 8h22M4 8l-3 8h6zM26 8l-3 8h6z"/></svg></div>
      <h3>Commercially Neutral</h3>
      <p>We are not run by any carrier or reseller, so there is no conflict of interest with members. We treat every network provider fairly and publish clear technical requirements for all.</p>
    </div>
    <div class="feature">
      <div class="feature-icon"><svg width="30" height="30" viewBox="0 0 30 30" fill="#1f7dc6"><path d="M15 2a9 9 0 0 0-9 9c0 7 9 17 9 17s9-10 9-17a9 9 0 0 0-9-9zm0 13a4 4 0 1 1 0-8 4 4 0 0 1 0 8z"/></svg></div>
      <h3>Australia Wide</h3>
      <p>Corvane Link exchanges are located in every major city. With a presence in 11 data centre across the nation, you are bound to find a well-connected point close to you.</p>
    </div>
  </div>
</section>

<section class="benefits">
  <div class="wrap">
    <div class="person-photo" role="img" aria-label="Photo of a smiling businessman in a suit, arms crossed"></div>
    <ul class="benefit-list">
      <li class="benefit"><span class="benefit-icon"><svg width="10" height="10" viewBox="0 0 10 10"><path d="M1 5l3 3 5-6" fill="none" stroke="#1f7dc6" stroke-width="2"/></svg></span><div><h4>Peering Points Across the Nation</h4><p>All Corvane Link exchanges are built to a shared standard, giving members consistent peering at every site and a simple way to reach local networks in each state.</p></div></li>
      <li class="benefit"><span class="benefit-icon"><svg width="10" height="10" viewBox="0 0 10 10"><path d="M1 5l3 3 5-6" fill="none" stroke="#1f7dc6" stroke-width="2"/></svg></span><div><h4>Multilateral Peering Points</h4><p>Route servers at each exchange let members peer with many networks from one session, reducing setup work and keeping traffic local.</p></div></li>
      <li class="benefit"><span class="benefit-icon"><svg width="10" height="10" viewBox="0 0 10 10"><path d="M1 5l3 3 5-6" fill="none" stroke="#1f7dc6" stroke-width="2"/></svg></span><div><h4>Members Services</h4><p>Being member owned allows us to focus on services that benefit the whole community, with support and tools shaped by member feedback.</p></div></li>
      <li class="benefit"><span class="benefit-icon"><svg width="10" height="10" viewBox="0 0 10 10"><path d="M1 5l3 3 5-6" fill="none" stroke="#1f7dc6" stroke-width="2"/></svg></span><div><h4>Not For Profit</h4><p>Fees cover running costs only. Any surplus is reinvested into the exchanges and into programs that support the local internet community.</p></div></li>
      <li class="benefit"><span class="benefit-icon"><svg width="10" height="10" viewBox="0 0 10 10"><path d="M1 5l3 3 5-6" fill="none" stroke="#1f7dc6" stroke-width="2"/></svg></span><div><h4>Strong Membership Base</h4><p>From small regional providers to large content networks, our members make each exchange more valuable by bringing more routes together.</p></div></li>
    </ul>
  </div>
</section>

<section class="news">
  <div class="wrap">
    <div class="blog">
      <h2 class="section-title">Latest Blog Posts</h2>
      <article class="post">
        <div class="post-thumb" role="img" aria-label="Blog post thumbnail photo"></div>
        <div>
          <h5>New Exchange Opens in Darwin</h5>
          <p>Members can now connect at our newest site, bringing local peering to the top end with the same service standards as every other exchange.</p>
        </div>
      </article>
      <a href="#" class="read-more">▸ Read More</a>
    </div>
    <div class="testimonials">
      <h2 class="section-title">Testimonials</h2>
      <div class="quote">
        <div class="quote-mark">“</div>
        <p>Corvane Link has been a reliable partner for our network for many years. Joining was simple, the team is responsive, and peering locally has improved speeds for our customers while lowering our transit costs.</p>
      </div>
      <div class="quote-author">
        <div><strong>Mr. Harlan Doyle</strong><small>Network Manager</small></div>
        <div class="avatar" role="img" aria-label="Portrait photo of the reviewer"></div>
      </div>
    </div>
  </div>
</section>

<section class="partners">
  <div class="wrap">
    <span class="partner">Parallax Edge</span>
    <span class="partner">Northwind Soft</span>
    <span class="partner">vendora.example</span>
    <span class="partner">Quorix</span>
    <span class="partner">Brightline Net</span>
  </div>
</section>

<footer class="site-footer">
  <div class="wrap">
    <div class="touch">
      <h3>Get In Touch With Us</h3>
      <p class="lead">If you wish to contact us please send us a message using the details below.</p>
      <div class="touch-body">
        <ul class="touch-list">
          <li><svg width="10" height="12" viewBox="0 0 10 12"><path d="M5 0a5 5 0 0 0-5 5c0 3 5 7 5 7s5-4 5-7a5 5 0 0 0-5-5z" fill="#1f7dc6"/></svg>48 Harbourline Road, Northgate WA 6000</li>
          <li><svg width="12" height="9" viewBox="0 0 12 9"><rect x=".5" y=".5" width="11" height="8" fill="none" stroke="#1f7dc6"/><path d="M.5.5l5.5 4 5.5-4" fill="none" stroke="#1f7dc6"/></svg>hello@corvanelink.example</li>
          <li><svg width="10" height="10" viewBox="0 0 10 10"><path d="M2 0l2 2-1 2c1 1 2 2 3 3l2-1 2 2-2 2C4 10 0 6 0 2z" fill="#1f7dc6"/></svg>+61 8 5550 0142<br>+61 8 5550 0143</li>
        </ul>
        <div class="map" role="img" aria-label="Street map showing the office location"></div>
      </div>
    </div>
    <div class="social">
      <h3>Stay Connected !</h3>
      <p class="lead">You can connect with us through a variety of our online social networks.</p>
      <div class="social-grid">
        <span class="social-btn"><i></i>Network Page</span>
        <span class="social-btn"><i></i>Short Posts</span>
        <span class="social-btn"><i></i>Careers</span>
        <span class="social-btn"><i></i>Photos</span>
        <span class="social-btn"><i></i>Circles</span>
        <span class="social-btn"><i></i>News Feed</span>
      </div>
    </div>
  </div>
</footer>

<div class="bottom-bar">© 2015 Corvane Link – Tallowmere Network Society Inc. All rights reserved.</div>

</body>
</html>
```